Brochure Design Project BiFold DL- Health/Exercise

Instruction brochure for using a massage tool.

BiFOLD DL size brochure. i believe this size should fit all the info, i have cut some info out to make it fit. However, if you think it needs a bigger size like a triFOLD DL size, please let me know, i am happy to do either.

Colors to use can be any combination of orange, black, white and also grey is ok as this will match the theme of the webpage which is still yet to be published.

Target Market(s)

all adults. 18 yrs and older

Industry/Entity Type

Massage

Requirements
Must have
• all the pictures are needed in the brochure... except the picture of the massage tool itself.

I have included 2 pictures of the massage tool, you may choose one, or even none if you think it looks better without it. The instruction brochure will come with the massage tool so therefore it is not entirely necessary to have that picture included.

DL size bifold, thus there will be 4 pages i total. But as i mentioned earlier it can be changed to 6 pages if need more space? but it should fit i think
Nice to have
• any other pictures of back pain etc would be nice

```html
<!DOCTYPE html>
<html lang="en">
<head>
<meta charset="utf-8">
<title>Vertaroll – Directions of use</title>
<link href="https://fonts.googleapis.com/css2?family=Montserrat:wght@600;700&family=Raleway:wght@400;500&display=swap" rel="stylesheet">
<style>
  :root {
    --orange: #ee8427;
    --orange-soft: #fbe0c6;
    --ink: #1f1f1f;
    --text: #3d3d3d;
    --paper: #ffffff;
    --illus-skin: #e3b48c;
    --illus-suit: #2d3a6e;
  }
  * { box-sizing: border-box; margin: 0; padding: 0; }
  html, body { width: 1200px; height: 1000px; overflow: hidden; }
  body {
    position: relative;
    background: var(--paper);
    font-family: "Raleway", Arial, sans-serif;
    color: var(--text);
    font-size: 14px;
    letter-spacing: 0.15px;
    line-height: 18.5px;
  }
  .frame-band {
    position: absolute; left: 0; width: 1200px; height: 75px;
    background: linear-gradient(180deg, #2b2927, #1c1b1a);
  }
  .frame-band--top { top: 0; }
  .frame-band--bottom { top: 925px; }
  .title-bar {
    position: absolute; top: 75px; left: 0; width: 1200px; height: 60px;
    background: var(--orange);
  }
  .title-bar h1 {
    position: absolute; left: 40px; top: 38px;
    font-family: "Montserrat", Arial, sans-serif; font-weight: 700;
    font-size: 14px; color: var(--paper); line-height: 18px; letter-spacing: 0;
  }
  .column { position: absolute; }
  .column--one { left: 40px; top: 143px; width: 340px; line-height: 16px; }
  .column--two { left: 428px; top: 143px; width: 342px; }
  .step-title {
    font-family: "Montserrat", Arial, sans-serif; font-weight: 600;
    font-size: 14.5px; color: var(--ink); line-height: 18px; margin-bottom: 10px;
    letter-spacing: 0;
  }
  .steps { list-style: none; }
  .steps li { position: relative; padding-left: 26px; margin-bottom: 12px; }
  .steps li::before {
    content: ""; position: absolute; left: 4px; top: 5px;
    width: 8px; height: 8px; background: var(--orange);
  }
  .illustration {
    position: absolute;
    background: linear-gradient(135deg, var(--illus-suit) 0%, #5a5f86 45%, var(--illus-skin) 100%);
    opacity: .35; border-radius: 6px;
  }
  .illustration--find { left: 40px; top: 398px; width: 335px; height: 157px; }
  .illustration--release { left: 485px; top: 487px; width: 240px; height: 370px; }
  .illustration--retest { left: 836px; top: 695px; width: 328px; height: 158px; }
  .placement { position: absolute; left: 40px; top: 575px; width: 340px; line-height: 17.3px; }
  .spine-diagram {
    float: right; width: 188px; height: 157px; margin: 0 0 6px 10px;
    border: 1px solid #bdbdbd;
    background: linear-gradient(90deg, #e6e6e6 0%, #d9d9d9 45%, #f0c7bd 60%, #e6e6e6 100%);
  }
  .usage-card {
    position: absolute; left: 836px; top: 348px; width: 324px; height: 162px;
    background: var(--orange); padding: 17px 20px 0 21px;
  }
  .usage-card h2 {
    font-family: "Raleway", Arial, sans-serif; font-weight: 500;
    font-size: 22px; color: var(--paper); line-height: 26px; margin-bottom: 6px;
  }
  .usage-card p { color: var(--orange-soft); }
  .product-photo {
    position: absolute; left: 900px; top: 165px; width: 200px; height: 200px;
    border-radius: 50%;
    background: radial-gradient(circle at 50% 45%, #d9b27a 0%, #c79a5e 35%, #e2e2e2 62%, #cfcfcf 100%);
  }
  .retest { position: absolute; left: 836px; top: 547px; width: 324px; }
  .copyright {
    position: absolute; right: 40px; top: 871px;
    color: var(--orange); font-size: 14px;
  }
</style>
</head>
<body>
  <div class="frame-band frame-band--top"></div>

  <header class="title-bar"><h1>Directions of use</h1></header>

  <section class="column column--one">
    <h3 class="step-title">1. Find the Restriction</h3>
    <ul class="steps">
      <li>Lie on your back on a firm surface, such as the floor, with knees bent to approximately 90 degrees.</li>
      <li>Swing your knees from side to side to assess for a pulling or tightness on either side of the spine</li>
      <li>If you are unable to detect any tightness or restriction, bring your knees to your chest first and then swing them to either side</li>
      <li>If you are still unable to detect any restriction, consult a qualified practitioner who will assess for any restriction</li>
    </ul>
  </section>

  <div class="illustration illustration--find" role="img" aria-label="Illustration of a woman lying on her back swinging bent knees side to side, and hugging knees to chest"></div>

  <section class="placement">
    <h3 class="step-title">2. Placement of Vertaroll™</h3>
    <ul class="steps">
      <li><div class="spine-diagram" role="img" aria-label="Anatomical diagram of the spine with the tool's three domes placed beside the vertebrae over the deep spinal muscles"></div>Place the tool vertically with the middle apex on the side directly over the most restrictive point adjacent to the spinal column (this will usually be directly on the joint and over the deep spinal muscles); this can be placed over clothing for comfort</li>
      <li>Allow your back to relax down over the tool</li>
    </ul>
  </section>

  <section class="column column--two">
    <h3 class="step-title">3. Active Release</h3>
    <ul class="steps">
      <li>Bring the knee on the same side as the tool to your chest, this will feel like an increased tension over the area of the tool due to the muscle being stretched, hold for 2-3 seconds then release, and repeat 8-10 times (you may also choose to bring both knees up instead)</li>
      <li>If you do not feel much of an increased tension under the tool, you can instead lift your bottom whilst pushing your back down into the tool; hold for 2-3 seconds and repeat 8-10 times</li>
      <li>The tension under the area of the tool should not decrease at any time, if this occurs consult a qualified practitioner to check on your technique</li>
    </ul>
  </section>

  <div class="illustration illustration--release" role="img" aria-label="Three illustrations of a woman lying on her back: both knees to chest, one knee to chest, and lifting her hips"></div>

  <aside class="usage-card">
    <h2>Usage</h2>
    <p>Recommended usage is once a day, every 2-3 days until you no longer feel a tightness or restriction during the active range of motion testing; or as otherwise directed by your practitioner.</p>
  </aside>

  <div class="product-photo" role="img" aria-label="Photo of the wooden massage tool with three rounded domes"></div>

  <section class="retest">
    <h3 class="step-title">4. Retest</h3>
    <p>Retest the same active range of motion testing you did at the start when you found your restriction. You should find a reduction or ease in the pulling/tightness and improved range of motion than at the start.</p>
  </section>

  <div class="illustration illustration--retest" role="img" aria-label="Illustration of a woman repeating the knee swing and knees-to-chest tests"></div>

  <p class="copyright">© Vertaroll™ 2013</p>

  <div class="frame-band frame-band--bottom"></div>
</body>
</html>
```